New bussiness card, using company logo.
Lachlan Voss
Manager/Director
Birch Property Developments
Po Box 4657
Marlowe Central
Nrd
0455 386 218
lachlan@birchpropertydevelopments
eye catching, vibrant colours, professional

```html
<!DOCTYPE html>
<html lang="en">
<head>
<meta charset="utf-8">
<title>Lachlan Voss – Business Card</title>
<link rel="stylesheet" href="https://fonts.googleapis.com/css2?family=Nunito:wght@300;400;700&display=swap">
<style>
  :root {
    --canvas-bg: #d6d6d6;
    --card-dark: #2b2829;
    --text-light: #d9d9d9;
    --text-muted: #bdbdbd;
    --brand-green: #6cc24a;
    --brand-red: #e2333f;
    --band-white: #f4f4f4;
    --white: #ffffff;
  }
  * { box-sizing: border-box; margin: 0; padding: 0; }
  html, body {
    width: 1200px;
    height: 900px;
    overflow: hidden;
    background: var(--canvas-bg);
    font-family: "Nunito", "Helvetica Neue", Arial, sans-serif;
  }
  .canvas {
    position: relative;
    width: 1200px;
    height: 900px;
  }
  .card {
    position: absolute;
    left: 280px;
    width: 640px;
    height: 390px;
    background: var(--card-dark);
    overflow: hidden;
    box-shadow: 0 6px 18px rgba(0,0,0,0.25);
  }
  .card--outline { top: 40px; }
  .card--banded  { top: 470px; }

  .identity {
    position: absolute;
    left: 34px;
    top: 30px;
  }
  .identity__name {
    display: inline-block;
    font-weight: 700;
    font-size: 24px;
    letter-spacing: 0.3px;
    padding-bottom: 4px;
    border-bottom: 2px solid currentColor;
  }
  .identity__role {
    margin-top: 26px;
    font-size: 19px;
    font-weight: 300;
  }
  .identity__company {
    margin-top: 24px;
    font-size: 17px;
    font-weight: 300;
  }
  .address {
    position: absolute;
    right: 34px;
    top: 56px;
    text-align: right;
    font-style: normal;
    font-weight: 300;
    font-size: 19px;
    line-height: 1.45;
  }

  .card--outline .identity,
  .card--outline .address { color: var(--text-light); }
  .card--outline .identity__role,
  .card--outline .identity__company { color: var(--text-muted); }

  .card--banded .identity,
  .card--banded .address { color: var(--brand-green); }

  .brand-mark {
    position: absolute;
    display: flex;
    align-items: center;
    gap: 12px;
    font-weight: 700;
    font-size: 22px;
    color: var(--brand-green);
    white-space: nowrap;
  }
  .brand-mark__square {
    width: 22px;
    height: 22px;
    background: var(--brand-green);
  }
  .card--outline .brand-mark {
    left: 50%;
    top: 240px;
    transform: translateX(-50%);
  }
  .card--banded .brand-mark {
    left: 34px;
    top: 50%;
    transform: translateY(-50%);
  }

  .stripe-green {
    position: absolute;
    left: 0;
    right: 0;
    background: var(--brand-green);
  }
  .card--outline .stripe-green { top: 310px; height: 9px; }

  .band-white {
    position: absolute;
    left: 0;
    right: 0;
    background: var(--band-white);
  }
  .card--banded .stripe-green { top: 238px; height: 12px; }
  .card--banded .band-white { top: 250px; height: 82px; }

  .contact-band {
    position: absolute;
    left: 0;
    right: 0;
    bottom: 0;
    background: var(--brand-red);
    color: var(--white);
    display: flex;
    align-items: center;
    justify-content: space-between;
    padding: 0 24px;
    font-size: 15px;
  }
  .card--outline .contact-band { top: 319px; }
  .card--banded .contact-band { top: 332px; }

  .contact-band__phone {
    display: flex;
    align-items: center;
    gap: 8px;
  }
  .icon-phone { width: 14px; height: 14px; }
</style>
</head>
<body>
<main class="canvas">

  <section class="card card--outline" aria-label="Business card, dark variant">
    <div class="identity">
      <h1 class="identity__name">Lachlan Voss</h1>
      <p class="identity__role">Manager/Director</p>
      <p class="identity__company">Birch Property Developments</p>
    </div>
    <address class="address">P.O. Box 4657<br>Marlowe Central<br>Nrd</address>
    <div class="brand-mark">
      <span class="brand-mark__square"></span>
      <span class="brand-mark__name">Birch Property Developments</span>
    </div>
    <div class="stripe-green"></div>
    <div class="contact-band">
      <span class="contact-band__phone">
        <svg class="icon-phone" viewBox="0 0 24 24" aria-hidden="true">
          <path fill="currentColor" d="M6.6 10.8a15.1 15.1 0 0 0 6.6 6.6l2.2-2.2c.3-.3.7-.4 1-.2 1.1.4 2.3.6 3.6.6.6 0 1 .4 1 1V20c0 .6-.4 1-1 1A17 17 0 0 1 3 4c0-.6.4-1 1-1h3.5c.6 0 1 .4 1 1 0 1.3.2 2.5.6 3.6.1.3 0 .7-.2 1l-2.3 2.2z"/>
        </svg>
        0455 386 218
      </span>
      <span class="contact-band__email">lachlan@birchpropertydevelopments.com</span>
    </div>
  </section>

  <section class="card card--banded" aria-label="Business card, banded variant">
    <div class="identity">
      <h2 class="identity__name">Lachlan Voss</h2>
      <p class="identity__role">Manager/Director</p>
      <p class="identity__company">Birch Property Developments</p>
    </div>
    <address class="address">P.O. Box 4657<br>Marlowe Central<br>Nrd</address>
    <div class="stripe-green"></div>
    <div class="band-white">
      <div class="brand-mark">
        <span class="brand-mark__square"></span>
        <span class="brand-mark__name">Birch Property Developments</span>
      </div>
    </div>
    <div class="contact-band">
      <span class="contact-band__phone">
        <svg class="icon-phone" viewBox="0 0 24 24" aria-hidden="true">
          <path fill="currentColor" d="M6.6 10.8a15.1 15.1 0 0 0 6.6 6.6l2.2-2.2c.3-.3.7-.4 1-.2 1.1.4 2.3.6 3.6.6.6 0 1 .4 1 1V20c0 .6-.4 1-1 1A17 17 0 0 1 3 4c0-.6.4-1 1-1h3.5c.6 0 1 .4 1 1 0 1.3.2 2.5.6 3.6.1.3 0 .7-.2 1l-2.3 2.2z"/>
        </svg>
        0455 386 218
      </span>
      <span class="contact-band__email">lachlan@birchpropertydevelopments.com</span>
    </div>
  </section>

</main>
</body>
</html>
```